Korvenna Building Inspections, Estimating & Project Management

Please read my capability statement uploaded in the files to get an indepth overview of who we are and what we do.
We are a construction company that is moving away from onsite construction to consultancy and inspection services. We will offer Building Inspections, Estimating Services, Project Management and Construction Management. We will still be working out in the field, however as inspectors and and coordinators only.
I am looking to build a website from scratch. I already have my logo built by pixel harbour previously and wish to remove the company slogan "Structures & Buildworks".
Background: Korvenna Pty Ltd is in the process of shutting down and re-registering as Korvenna Australia Pty Ltd. It will however retain all the original logos.
I do like websites like https://zenith.plorvatic-sample.com/#
I also do like to write all my emails in Roboto-Light font and open to suggestions on it's usage.
I currently host with Southland Webhosts and they use Wordpress 5.0

Target Market(s)

Home Owners Building or Renovating, Realestate Agents, Commercial Builders, Trades that require Estimating,

Industry/Entity Type

Construction

Coding

Number of Pages Required

Font styles to use
Other font styles liked:
• All fonts have been uploaded.

Requirements
Must have
• Must have the ability for monthly updates, photo uploads and industry tips I can share. A page dedicated to tips and understanding of what sets us apart from the competitors (this will require lots of input from me).
Nice to have
• I personally like pages like https://zenith.plorvatic-sample.com/# which have a background image and the foreground scrolling past. Open to suggestions here. A website that sets me apart of Brisbane rivals
Should not have
• Fixed pricing

```html
<!DOCTYPE html>
<html lang="en">
<head>
<meta charset="utf-8">
<title>Korvenna Australia</title>
<link href="https://fonts.googleapis.com/css2?family=Roboto:wght@300;400;500;700;900&display=swap" rel="stylesheet">
<style>
:root{
  --yellow:#fbbc04;
  --ink:#1c1c1c;
  --body:#4a4a4a;
  --dark:#2a292d;
  --darker:#1f1f20;
  --white:#ffffff;
  --rule:#e4e4e4;
}
*{margin:0;padding:0;box-sizing:border-box}
html,body{width:1200px;height:2250px;overflow:hidden;background:var(--white)}
body{position:relative;font-family:"Roboto",sans-serif;color:var(--ink)}
.abs{position:absolute}
.photo{position:absolute}
.eyebrow{position:absolute;font-size:9.5px;font-weight:500;color:var(--yellow)}
.title{position:absolute;font-size:13.5px;font-weight:500;color:var(--ink)}
.title .accent{color:var(--yellow)}
.underline{position:absolute;width:50px;height:2px;background:var(--yellow)}
.copy{position:absolute;font-size:9.3px;font-weight:300;line-height:15px;color:var(--body)}
.btn{position:absolute;height:25px;background:var(--yellow);color:var(--ink);font-size:7.8px;font-weight:500;letter-spacing:.3px;display:flex;align-items:center;justify-content:center;text-transform:uppercase}
.facts{position:absolute;left:0;top:837px;width:1200px;height:287px;background:linear-gradient(90deg,#2f2e33 0%,#28272b 55%,#323136 100%)}
.facts .title,.facts .copy{color:var(--white)}
.facts .copy{font-weight:400}
.stat{position:absolute;top:75px;width:175px;height:137px;border:1.5px solid var(--yellow);text-align:center}
.stat .num{margin-top:32px;font-size:38px;font-weight:700;color:var(--yellow);line-height:1}
.stat .label{margin-top:14px;font-size:9.5px;font-weight:500;color:var(--white);letter-spacing:.4px}
.ghost-name{position:absolute;font-size:28px;font-weight:900;color:#e6e6e6;letter-spacing:1px}
.mark{position:absolute;display:flex;align-items:center;gap:8px;font-size:16px;font-weight:700;color:#3d3d3d}
.mark i{display:block;width:18px;height:18px;background:var(--yellow)}
.bullets{position:absolute;list-style:none;font-size:9.3px;font-weight:300;color:var(--body)}
.bullets li{height:22px;display:flex;align-items:center;gap:8px}
.bullets li::before{content:"";width:6px;height:6px;border-radius:50%;background:var(--yellow)}
.partners{position:absolute;left:0;top:1695px;width:1200px;height:292px;background:var(--darker)}
.partner{position:absolute;top:75px;width:153px;height:88px;background:#141414;display:flex;align-items:center;justify-content:center;gap:8px;color:var(--white);font-size:13px;font-weight:700}
.partner i{display:block;width:12px;height:12px;background:var(--white)}
.cta{position:absolute;left:181px;top:1934px;width:838px;height:114px;background:var(--yellow)}
.cta .eyebrow{color:var(--white);font-weight:700}
.cta .divider{position:absolute;left:222px;top:31px;width:2px;height:51px;background:var(--white)}
.cta .copy{color:#2b2b2b;font-weight:400}
.btn.dark{background:var(--ink);color:var(--white)}
.info-label{position:absolute;top:2102px;font-size:8.5px;color:var(--body)}
.info-value{position:absolute;top:2118px;font-size:9.8px;color:var(--ink)}
.footer-rule{position:absolute;left:181px;top:2166px;width:838px;height:1px;background:var(--rule)}
.copyright{position:absolute;left:0;top:2204px;width:1200px;text-align:center;font-size:8.5px;color:var(--body)}
</style>
</head>
<body>

<!-- Consultation -->
<div class="photo" style="left:181px;top:74px;width:419px;height:344px;background:linear-gradient(135deg,#4a6fa5 0%,#b5604a 45%,#c9b48a 100%)" role="img" aria-label="Two inspectors in hard hats looking up at a brick wall on site"></div>
<div class="eyebrow" style="left:618px;top:134px">22 Years Experience</div>
<div class="title" style="left:618px;top:153px">Korvenna Offers Consultations to Support.</div>
<div class="underline" style="left:619px;top:185px"></div>
<p class="copy" style="left:619px;top:215px;width:398px">With over 22 years of industry experience, our expert team delivers exceptional, efficient, and innovative solutions tailored to your project needs. Committed to client satisfaction, we build lasting relationships based on integrity, trust, and transparency.</p>
<p class="copy" style="left:619px;top:275px;width:398px">Korvenna offers consultations to support how our expertise can turn your project visions into a reality.</p>
<div class="btn" style="left:619px;top:333px;width:105px">View All Services</div>

<!-- Vision -->
<div class="photo" style="left:600px;top:418px;width:419px;height:344px;background:linear-gradient(160deg,#3f64a8 0%,#8a6a55 50%,#d7c9a3 100%)" role="img" aria-label="Inspector with plans talking with a builder in a hard hat outside new homes"></div>
<div class="eyebrow" style="left:181px;top:485px">South East Queensland</div>
<div class="title" style="left:181px;top:504px">Our Vision Is To Be The Foremost Company.</div>
<div class="underline" style="left:182px;top:536px"></div>
<p class="copy" style="left:182px;top:566px;width:398px">At Korvenna Australia Pty Ltd, our vision is to be the foremost construction company in South East Queensland, renowned for our unparalleled expertise.</p>
<p class="copy" style="left:182px;top:611px;width:405px">We aim to lead the industry by delivering integrated, specialized services across building &amp; pest inspections, estimating, project management, and construction management.</p>
<div class="btn" style="left:182px;top:669px;width:105px">View All Services</div>

<!-- Facts -->
<section class="facts" role="img" aria-label="Dark backdrop of hands reviewing building plans on a table">
  <div class="eyebrow" style="left:181px;top:73px;font-weight:700">You Need To Know</div>
  <div class="title" style="left:181px;top:93px">Few Fun Fact About Korvenna</div>
  <div class="underline" style="left:182px;top:125px"></div>
  <p class="copy" style="left:182px;top:154px;width:205px">We want people to thrive at Korvenna we believe you do your best work when you feel your best. Here are a just a few benefits we're proud to provide our team.</p>
  <div class="stat" style="left:443px"><div class="num">22+</div><div class="label">YEARS EXPERIENCE</div></div>
  <div class="stat" style="left:644px"><div class="num">1,200+</div><div class="label">COMPLETED PROJECTS</div></div>
  <div class="stat" style="left:844px"><div class="num">300+</div><div class="label">HAPPY CLIENTS</div></div>
</section>

<!-- About -->
<div class="photo" style="left:181px;top:1199px;width:195px;height:250px;background:linear-gradient(135deg,#c4543a 0%,#a7866a 50%,#d2cfa4 100%)" role="img" aria-label="Smiling inspector gesturing beside a builder at a brick site"></div>
<div class="ghost-name" style="left:181px;top:1458px">KORVENNA</div>
<div class="mark" style="left:396px;top:1310px"><i></i>Korvenna</div>
<div class="photo" style="left:396px;top:1370px;width:195px;height:250px;background:linear-gradient(180deg,#6e8a86 0%,#d8d4cc 55%,#c86a3a 100%)" role="img" aria-label="Builder in high-visibility vest and inspector inside a house under construction"></div>

<div class="eyebrow" style="left:618px;top:1198px;font-weight:700">Why Choose Us ?</div>
<div class="title" style="left:618px;top:1217px">About <span class="accent">Korvenna</span> Australia</div>
<div class="underline" style="left:619px;top:1249px"></div>
<p class="copy" style="left:619px;top:1279px;width:400px">With Korvenna Australia Pty Ltd, you gain peace of mind knowing that your property is safe, sound, and compliant. Unlike tick-a-flick inspectors who rush through checklists, our inspections are conducted by a seasoned builder with over 22 years of hands-on industry experience and a keen eye for detail. We uphold the highest quality standards, ensuring no detail is overlooked.</p>
<p class="copy" style="left:619px;top:1354px;width:400px">Our expert takes genuine pride in his work, meticulously assessing every aspect of a property with the same care and diligence he would for his own projects. We don't just identify issues we provide clear, actionable insights to help you make informed decisions with confidence.</p>
<ul class="bullets" style="left:619px;top:1413px">
  <li>Industry Expertise – Our inspectors bring over 22 years of hands-on experience.</li>
  <li>Advanced Technology – We leverage state-of-the-art tools for precise assessments.</li>
  <li>Useful Reports – Receive clear, easy-to-understand findings with actionable insights.</li>
  <li>Fast Turnaround – Get reports quickly to make informed decisions.</li>
  <li>Customer-Focused – Providing tailored advice to help you navigate inspection findings.</li>
</ul>
<p class="copy" style="left:619px;top:1538px;width:400px">Buying, selling, building, or investing? Let Korvenna Australia simplify the process. Contact us today to discuss your project and discover the expertise that makes us industry leaders.</p>
<div class="btn" style="left:619px;top:1596px;width:109px">Contact Us Today</div>

<!-- Partners -->
<section class="partners">
  <div class="partner" style="left:181px"><i></i>Trelbrook Builds</div>
  <div class="partner" style="left:352px"><i></i>Trelbrook Builds</div>
  <div class="partner" style="left:524px"><i></i>Trelbrook Builds</div>
  <div class="partner" style="left:695px"><i></i>Trelbrook Builds</div>
  <div class="partner" style="left:866px"><i></i>Trelbrook Builds</div>
</section>

<!-- Call to action -->
<section class="cta">
  <div class="eyebrow" style="left:37px;top:38px">Dont Waste Your Time!</div>
  <div class="title" style="left:37px;top:58px;font-size:13.5px">Get an Inspecton Today!</div>
  <div class="divider"></div>
  <p class="copy" style="left:261px;top:33px;width:395px;font-size:9.5px;line-height:16px">Submit a request online today to arrange a top rated building expert. We're always ready to assist with queries, offer a quote, and keep your property safe and compliant. Gain confidence with expert inspections across Australia.</p>
  <div class="btn dark" style="left:695px;top:41px;width:105px">Contact Us Now</div>
</section>

<!-- Footer -->
<div class="info-label" style="left:181px">Phone</div>
<div class="info-value" style="left:181px">+61 100 482 915</div>
<div class="info-label" style="left:367px">Email</div>
<div class="info-value" style="left:367px">info@korvennaaustralia.com.au</div>
<div class="info-label" style="left:618px">Address</div>
<div class="info-value" style="left:618px">PO Box 18, Carrowvale, Q, 4999, Australia</div>
<div class="info-label" style="left:892px">Follow Us</div>
<div class="info-value" style="left:892px">Chatterbox, Snapwall, Clipstream</div>
<div class="footer-rule"></div>
<div class="copyright">© Copyright 2025 Korvenna Australia | Brightloom Studio.</div>

</body>
</html>
```